Web design for a job listing site

We have developed a simple job listings site and need a designer to mock up a look and feel for it. We already have a logo and fonts picked out. We need design ideas for the overall look and feel as well as the header, footer and navigation elements.
The header should have our logo, a site navigation with drop-down capabilities, an account section which is a user icon that engages a drop down menu.
Bellow the header there will be the content section which will have two columns. The left section will take up 2/3 or 9 columns in a twelve column system and the right section will take up 1/3 or 3 columns.
In the left section there will be a search bar on top and listings below that very similar to http://www.bravelinkwork.com/ except we would like to appear more modern and sharp.
In the right section there will be a call to action for a new job posting at the top and an activity feed below that followed by a banner add.
Finally there is the footer which should be simple and contain copy write info and links. All content can be mocked with Lorem Ipsum.
We have attached our current logo as well as some screen grabs from the development site.
As a note the logo uses the Cinzel font which is all caps so another font must be used for the non header content. Currently we are using Droid Serif though we are open to other ideas.
Target Market(s)
We need to appeal to people looking for work and employers seeking professionals
Industry/Entity Type
Call
Colors
Designer to choose colors to be used in the design.
Look and feel

```html
<!DOCTYPE html>
<html lang="en">
<head>
<meta charset="utf-8">
<title>Greenleaf Jobs</title>
<link href="https://fonts.googleapis.com/css2?family=Cinzel:wght@400;700&family=Lato:wght@400;700;900&display=swap" rel="stylesheet">
<style>
:root{
  --green:#2f7f33;
  --green-dark:#236a27;
  --green-light:#6aa842;
  --green-text:#2a7a2e;
  --page-bg:#f1f1ef;
  --white:#ffffff;
  --ink:#333333;
  --muted:#777777;
  --line:#c9c9c9;
  --blue:#3b78b8;
  --sky:#3aa3d8;
  --red:#a51e22;
  --charcoal:#3a3a3a;
  --olive:#6a9e3c;
  --band:#dcdcda;
}
*{box-sizing:border-box;margin:0;padding:0}
html,body{width:721px;height:1200px;overflow:hidden;background:var(--page-bg)}
body{font-family:'Lato',sans-serif;color:var(--ink)}
.page{position:relative;width:769px;height:1280px;transform:scale(0.93758);transform-origin:0 0;background:var(--page-bg)}
.abs{position:absolute}

/* top navigation */
.top-nav{left:0;top:0;width:769px;height:24px;background:var(--green);display:flex;justify-content:center}
.top-nav ul{display:flex;list-style:none;width:620px;justify-content:space-between;align-items:center}
.top-nav li{font-size:9px;color:var(--white);position:relative}
.top-nav li+li::before{content:"";position:absolute;left:-13px;top:-2px;height:13px;border-left:1px solid rgba(255,255,255,.3)}

/* header */
.site-header{left:0;top:24px;width:769px;height:62px;background:var(--white)}
.brand{left:86px;top:18px;display:flex;align-items:center;gap:8px}
.brand-mark{width:22px;height:22px;border-radius:50%;background:var(--green)}
.brand-name{font-family:'Lato',sans-serif;font-weight:900;font-size:22px;color:var(--green);letter-spacing:1px}
.header-btn{left:613px;width:73px;height:17px;background:linear-gradient(#4c9e3e,#2d7a2c);color:var(--white);font-size:8px;font-weight:700;display:flex;align-items:center;justify-content:center;border-radius:2px}

/* hero */
.hero{left:0;top:86px;width:769px;height:192px;background:linear-gradient(90deg,#1b2e48 0%,#2c4a6e 35%,#2b4a6c 60%,#1d3452 100%);overflow:hidden}
.hero-visual{position:absolute;left:60px;top:0;width:340px;height:192px;background:radial-gradient(ellipse at 40% 50%,rgba(90,150,210,.55),rgba(40,80,130,0) 70%)}
.hero-title{position:absolute;left:400px;top:70px;width:290px;text-align:center;font-family:'Cinzel',serif;font-size:22px;line-height:30px;color:var(--white);letter-spacing:.5px}
.hero-dots{position:absolute;left:518px;top:142px;display:flex;gap:5px}
.hero-dots span{width:10px;height:10px;border-radius:50%;background:var(--white)}
.hero-dots span.active{background:var(--green);border:2px solid var(--white)}

/* category bar */
.category-bar{left:0;top:278px;width:769px;height:23px;background:var(--green);display:flex;justify-content:center}
.category-bar ul{display:flex;list-style:none;width:601px}
.category-bar li{flex:1;font-size:10px;color:var(--white);display:flex;align-items:center;justify-content:center;position:relative}
.category-bar li+li::before{content:"";position:absolute;left:0;top:6px;height:11px;border-left:1px solid rgba(255,255,255,.25)}
.category-bar li.current{background:var(--green-light);flex:0 0 86px}

/* search */
.search-panel{left:85px;top:301px;width:601px;height:43px;background:var(--white);box-shadow:0 1px 3px rgba(0,0,0,.15)}
.field{position:absolute;top:14px;height:16px;border:1px solid var(--line);border-radius:3px;font-size:8px;font-style:italic;color:#555;padding-left:9px;display:flex;align-items:center}
.search-btn{position:absolute;left:466px;top:13px;width:18px;height:17px;background:var(--green);border-radius:2px}
.radius-label{position:absolute;left:498px;top:17px;font-size:8.5px;color:#555}
.radius-select{position:absolute;left:537px;top:14px;width:51px;height:16px;border:1px solid var(--line);font-size:8px;font-style:italic;color:#555;padding-left:5px;display:flex;align-items:center}
.radius-select::after{content:"";position:absolute;right:0;top:0;width:15px;height:14px;background:var(--green)}
.radius-select svg{position:absolute;right:3px;top:4px;z-index:1}

/* listings */
.listings{left:85px;top:367px;width:450px;height:779px;background:var(--white)}
.tabs{display:flex;height:22px}
.tab{color:var(--white);font-size:12px;font-weight:700;display:flex;align-items:center;justify-content:center;background:var(--green-dark);border-right:1px solid #fff}
.tab.active{background:var(--green-light);position:relative}
.tab.active::after{content:"";position:absolute;left:46px;bottom:-5px;border:5px solid transparent;border-bottom:0;border-top-color:var(--green-light)}
.job{position:absolute;left:12px;width:424px;height:34px;border:1px dashed #c8c8c8}
.badge{position:absolute;left:6px;top:8px;width:72px;height:17px;border-radius:2px;color:var(--white);font-size:9px;display:flex;align-items:center;justify-content:center}
.badge.full{background:var(--blue)}
.badge.commission{background:var(--sky)}
.badge.contract{background:var(--red)}
.badge.part{background:var(--charcoal)}
.badge.part-green{background:var(--olive)}
.job-title{position:absolute;left:89px;top:5px;font-size:9px;font-weight:700;color:var(--green-text)}
.job-meta{position:absolute;left:89px;top:18px;font-size:7.5px;color:#666}
.job-loc{position:absolute;left:273px;top:5px;font-size:8.5px;line-height:12px;color:#444}
.job-date{position:absolute;left:367px;top:11px;font-size:8.5px;font-weight:700;color:var(--green-text)}
.pager{position:absolute;left:0;bottom:0;width:450px;height:22px;background:var(--green);display:flex;justify-content:center;align-items:center;gap:8px;color:#8ecb6a;font-size:12px;font-weight:700}
.pager .now{background:var(--green-light);color:var(--white);width:20px;height:22px;display:flex;align-items:center;justify-content:center}

/* sidebar */
.widget{left:553px;width:133px;background:var(--white);box-shadow:0 0 2px rgba(0,0,0,.12)}
.widget-head{height:22px;background:var(--green);color:var(--white);font-size:12px;font-weight:700;display:flex;align-items:center;justify-content:center}
.price{text-align:center;padding-top:8px;font-size:11px;color:#333;line-height:17px}
.price strong{font-size:14px;font-weight:700}
.activity{position:absolute;left:9px;display:flex;gap:7px}
.avatar{width:34px;height:34px;border:1px solid #ddd;background:linear-gradient(#e9d7c3,#b98d6c)}
.activity p{font-size:7.5px;line-height:10px;width:78px;color:#333}
.scroller{position:absolute;left:6px;bottom:2px;width:121px;height:12px;border-top:1px solid #ddd}
.scroller span{position:absolute;left:17px;top:5px;width:30px;height:2px;background:#bbb}
.promo{font-size:13px;font-weight:700;line-height:15px}
.promo .a{position:absolute;left:10px;top:17px;color:var(--green-text)}
.promo .b{position:absolute;right:10px;top:64px;text-align:right;color:#222}
.promo .b em{font-style:normal;color:var(--green-text)}
.promo-deco{position:absolute;left:30px;top:6px;width:80px;height:98px;border-radius:50%;background:radial-gradient(circle,rgba(47,127,51,.12),rgba(47,127,51,0) 70%)}
.person-photo{position:absolute;left:9px;top:13px;width:42px;height:42px;border-radius:50%;border:2px solid var(--green);background:linear-gradient(#d9c3aa,#8a6a52)}
.person-name{position:absolute;left:62px;top:22px;font-size:10px;font-weight:700;color:#222}
.person-role{position:absolute;left:62px;top:37px;font-size:8px;color:#555}
.quote{position:absolute;left:9px;top:82px;width:115px;height:80px;border:1px solid #ddd;padding:10px 8px 0 16px;font-size:7.5px;font-style:italic;line-height:11px;color:#555;letter-spacing:.3px}
.quote-dots{position:absolute;left:85px;top:150px;display:flex;gap:3px}
.quote-dots span{width:4px;height:4px;border-radius:50%;background:#ccc}
.quote-dots span.on{background:var(--green)}
.ad-slot{position:absolute;left:6px;top:5px;width:121px;height:84px;background:linear-gradient(135deg,#1a1a1a,#5c2a1e 55%,#2a2a2a)}
.ad-title{position:absolute;left:0;top:3px;width:121px;text-align:center;font-family:'Lato',sans-serif;font-weight:900;font-size:20px;color:#c7d94a;letter-spacing:1px}

/* newsletter */
.newsletter{left:0;top:1172px;width:769px;height:41px;background:var(--band)}
.nl-icon{position:absolute;left:86px;top:7px;width:26px;height:26px;border-radius:50%;border:2px solid var(--green)}
.nl-title{position:absolute;left:120px;top:11px;font-size:16px;color:#222}
.nl-chevron{position:absolute;left:282px;top:5px}
.nl-copy{position:absolute;left:324px;top:15px;font-size:9.5px;color:#222}
.nl-input{position:absolute;left:475px;top:12px;width:156px;height:18px;background:var(--white);font-size:8px;color:#333;padding-left:6px;display:flex;align-items:center}
.nl-submit{position:absolute;left:636px;top:12px;width:49px;height:18px;background:var(--green);color:var(--white);font-size:8.5px;font-weight:700;display:flex;align-items:center;justify-content:center}

/* footer */
.site-footer{left:0;top:1213px;width:769px;height:67px;background:linear-gradient(var(--green),#2a7a2c);color:var(--white);text-align:center;font-size:8.5px}
.site-footer ul{list-style:none;display:flex;justify-content:center;gap:4px}
.site-footer li+li::before{content:"•";margin-right:4px}
.foot-row1{position:absolute;top:11px;width:100%}
.foot-row2{position:absolute;top:28px;width:100%}
.copyright{position:absolute;top:45px;width:100%;font-size:8px}
</style>
</head>
<body>
<div class="page">

  <nav class="top-nav abs">
    <ul>
      <li>About</li><li>My Jobs</li><li>Social Media</li><li>Blog</li><li>Login</li><li>Terms &amp; Conditions</li><li>FAQ</li><li>Banners</li><li>Contact</li><li>Tearms</li>
    </ul>
  </nav>

  <header class="site-header abs">
    <div class="brand abs"><span class="brand-mark"></span><span class="brand-name">GREENLEAF JOBS</span></div>
    <div class="header-btn abs" style="top:12px">SUBMIT A JOB</div>
    <div class="header-btn abs" style="top:34px">LOGIN | REGISTER</div>
  </header>

  <section class="hero abs">
    <div class="hero-visual" role="img" aria-label="Hand touching a glowing network of connected people icons"></div>
    <h1 class="hero-title">Lorem ipsum dolor sit<br>amet consectetuer</h1>
    <div class="hero-dots"><span></span><span class="active"></span><span></span><span></span></div>
  </section>

  <nav class="category-bar abs">
    <ul>
      <li class="current">Latest Jobs</li><li>Commission</li><li>Contract</li><li>Freelance</li><li>Full-Time</li><li>Part-Time</li><li>Temporary</li>
    </ul>
  </nav>

  <form class="search-panel abs">
    <div class="field" style="left:11px;width:217px">All Jobs</div>
    <div class="field" style="left:239px;width:217px">Location</div>
    <div class="search-btn"><svg width="18" height="17" viewBox="0 0 18 17"><circle cx="8" cy="7.5" r="3.5" fill="none" stroke="#fff" stroke-width="1.6"/><line x1="10.5" y1="10" x2="13" y2="12.5" stroke="#fff" stroke-width="1.8"/></svg></div>
    <span class="radius-label">Radius:</span>
    <div class="radius-select">Auto<svg width="9" height="6" viewBox="0 0 9 6"><path d="M0 0h9L4.5 6z" fill="#fff"/></svg></div>
  </form>

  <main class="listings abs">
    <div class="tabs">
      <div class="tab active" style="width:102px">Featured Jobs</div>
      <div class="tab" style="width:102px">Latest Jobs</div>
      <div class="tab" style="width:163px">Sponsored Job Listings</div>
    </div>

    <div class="job" style="top:35px"><span class="badge full">Full-Time</span><span class="job-title">Bud Tender</span><span class="job-meta">Harbor Row – Posted by Harbor Row</span><span class="job-loc">Los Angeles California,<br>United States</span><span class="job-date">5-FEB-2015</span></div>
    <div class="job" style="top:80px"><span class="badge commission">Commission</span><span class="job-title">Regional Sales Representative</span><span class="job-meta">Fieldline Co – Posted by Fieldline Co</span><span class="job-loc">Denver Colorado,<br>United States</span><span class="job-date">4-FEB-2015</span></div>
    <div class="job" style="top:125px"><span class="badge contract">Contract</span><span class="job-title">Advertising Executive – Michigan</span><span class="job-meta">Northway Press – Posted by Northway Media</span><span class="job-loc">Detroit Michigan,<br>United States</span><span class="job-date">3-FEB-2015</span></div>
    <div class="job" style="top:170px"><span class="badge part">Part-Time</span><span class="job-title">Patient Consultant</span><span class="job-meta">Verdant Staffing – Posted by Marcus Hale</span><span class="job-loc">Los Angeles California,<br>United States</span><span class="job-date">22-JAN-2015</span></div>
    <div class="job" style="top:215px"><span class="badge part-green">Part-Time</span><span class="job-title">Patient Liaison</span><span class="job-meta">Verdant Staffing – Posted by Marcus Hale</span><span class="job-loc">Los Angeles California,<br>United States</span><span class="job-date">22-JAN-2015</span></div>
    <div class="job" style="top:260px"><span class="badge full">Full-Time</span><span class="job-title">Bud Tender</span><span class="job-meta">Harbor Row – Posted by Harbor Row</span><span class="job-loc">Los Angeles California,<br>United States</span><span class="job-date">5-FEB-2015</span></div>
    <div class="job" style="top:305px"><span class="badge commission">Commission</span><span class="job-title">Regional Sales Representative</span><span class="job-meta">Fieldline Co – Posted by Fieldline Co</span><span class="job-loc">Denver Colorado,<br>United States</span><span class="job-date">4-FEB-2015</span></div>
    <div class="job" style="top:350px"><span class="badge contract">Contract</span><span class="job-title">Advertising Executive – Michigan</span><span class="job-meta">Northway Press – Posted by Northway Media</span><span class="job-loc">Detroit Michigan,<br>United States</span><span class="job-date">3-FEB-2015</span></div>
    <div class="job" style="top:395px"><span class="badge part">Part-Time</span><span class="job-title">Patient Consultant</span><span class="job-meta">Verdant Staffing – Posted by Marcus Hale</span><span class="job-loc">Los Angeles California,<br>United States</span><span class="job-date">22-JAN-2015</span></div>
    <div class="job" style="top:440px"><span class="badge part-green">Part-Time</span><span class="job-title">Patient Liaison</span><span class="job-meta">Verdant Staffing – Posted by Marcus Hale</span><span class="job-loc">Los Angeles California,<br>United States</span><span class="job-date">22-JAN-2015</span></div>
    <div class="job" style="top:485px"><span class="badge full">Full-Time</span><span class="job-title">Bud Tender</span><span class="job-meta">Harbor Row – Posted by Harbor Row</span><span class="job-loc">Los Angeles California,<br>United States</span><span class="job-date">5-FEB-2015</span></div>
    <div class="job" style="top:530px"><span class="badge commission">Commission</span><span class="job-title">Regional Sales Representative</span><span class="job-meta">Fieldline Co – Posted by Fieldline Co</span><span class="job-loc">Denver Colorado,<br>United States</span><span class="job-date">4-FEB-2015</span></div>
    <div class="job" style="top:583px"><span class="badge contract">Contract</span><span class="job-title">Advertising Executive – Michigan</span><span class="job-meta">Northway Press – Posted by Northway Media</span><span class="job-loc">Detroit Michigan,<br>United States</span><span class="job-date">3-FEB-2015</span></div>
    <div class="job" style="top:620px"><span class="badge part">Part-Time</span><span class="job-title">Patient Consultant</span><span class="job-meta">Verdant Staffing – Posted by Marcus Hale</span><span class="job-loc">Los Angeles California,<br>United States</span><span class="job-date">22-JAN-2015</span></div>
    <div class="job" style="top:665px"><span class="badge part-green">Part-Time</span><span class="job-title">Patient Liaison</span><span class="job-meta">Verdant Staffing – Posted by Marcus Hale</span><span class="job-loc">Los Angeles California,<br>United States</span><span class="job-date">22-JAN-2015</span></div>
    <div class="job" style="top:710px"><span class="badge full">Full-Time</span><span class="job-title">Bud Tender</span><span class="job-meta">Harbor Row – Posted by Harbor Row</span><span class="job-loc">Los Angeles California,<br>United States</span><span class="job-date">5-FEB-2015</span></div>

    <div class="pager">
      <svg width="8" height="10" viewBox="0 0 8 10"><path d="M7 0v10L0 5z" fill="#fff"/></svg>
      <span class="now">1</span><span>2</span><span>3</span><span>4</span>
      <svg width="8" height="10" viewBox="0 0 8 10"><path d="M1 0v10l7-5z" fill="#fff"/></svg>
    </div>
  </main>

  <aside>
    <section class="widget abs" style="top:367px;height:71px">
      <div class="widget-head">Submit a Job</div>
      <p class="price">Starting at<br><strong>$25.00</strong> for <strong>30 days</strong></p>
    </section>

    <section class="widget abs" style="top:449px;height:288px">
      <div class="widget-head">Recent Activity</div>
      <div class="activity" style="top:33px"><div class="avatar" role="img" aria-label="Member photo"></div><p>Lorem ipsum dolor sit amet, consectetuer adipiscing elit,</p></div>
      <div class="activity" style="top:80px"><div class="avatar" role="img" aria-label="Member photo"></div><p>Lorem ipsum dolor sit amet, consectetuer adipiscing elit,</p></div>
      <div class="activity" style="top:127px"><div class="avatar" role="img" aria-label="Member photo"></div><p>Lorem ipsum dolor sit amet, consectetuer adipiscing elit,</p></div>
      <div class="activity" style="top:174px"><div class="avatar" role="img" aria-label="Member photo"></div><p>Lorem ipsum dolor sit amet, consectetuer adipiscing elit,</p></div>
      <div class="activity" style="top:221px"><div class="avatar" role="img" aria-label="Member photo"></div><p>Lorem ipsum dolor sit amet, consectetuer adipiscing elit,</p></div>
      <div class="scroller">
        <svg class="abs" style="left:3px;top:2px" width="6" height="8" viewBox="0 0 6 8"><path d="M5 0L1 4l4 4" fill="none" stroke="#555" stroke-width="1.5"/></svg>
        <span></span>
        <svg class="abs" style="right:3px;top:2px" width="6" height="8" viewBox="0 0 6 8"><path d="M1 0l4 4-4 4" fill="none" stroke="#555" stroke-width="1.5"/></svg>
      </div>
    </section>

    <section class="widget promo abs" style="top:748px;height:109px">
      <div class="promo-deco"></div>
      <p class="a">Only $25 for a<br>Featured Job Post</p>
      <p class="b"><em>&amp; FREE for</em><br>Regular Posts!</p>
    </section>

    <section class="widget abs" style="top:868px;height:174px">
      <div class="widget-head">Testimonials</div>
      <div style="position:relative">
        <div class="person-photo" role="img" aria-label="Portrait of the reviewer"></div>
        <span class="person-name">Daniel Reyes</span>
        <span class="person-role">Bussiness Man</span>
        <p class="quote">Ut wisi enim ad minim veniam, quism nostrul ercitation ullamcorper suscipitop lobortis commod</p>
        <div class="quote-dots"><span></span><span class="on"></span><span></span><span></span></div>
      </div>
    </section>

    <section class="widget abs" style="top:1053px;height:94px">
      <div class="ad-slot" role="img" aria-label="Magazine advertisement showing a row of issue covers">
        <span class="ad-title">KESTREL</span>
      </div>
    </section>
  </aside>

  <section class="newsletter abs">
    <div class="nl-icon"><svg width="22" height="22" viewBox="0 0 22 22"><rect x="5" y="7" width="12" height="8" fill="none" stroke="#2f7f33" stroke-width="1.4"/><path d="M5 7l6 5 6-5" fill="none" stroke="#2f7f33" stroke-width="1.4"/></svg></div>
    <span class="nl-title">Newsletter Signup</span>
    <svg class="nl-chevron" width="28" height="30" viewBox="0 0 28 30"><path d="M2 2l12 13L2 28M12 2l12 13-12 13" fill="none" stroke="#c8c8c6" stroke-width="4"/></svg>
    <span class="nl-copy">Signup For Free Email Updates</span>
    <div class="nl-input">Enter your email here</div>
    <div class="nl-submit">SUBMIT</div>
  </section>

  <footer class="site-footer abs">
    <ul class="foot-row1"><li>About</li><li>My Jobs</li><li>Social Media</li><li>Blog</li><li>Login</li><li>Terms &amp; Conditions</li><li>FAQ</li><li>Banners</li><li>Contact</li><li>Tearms</li></ul>
    <ul class="foot-row2"><li>Latest Jobs</li><li>Commission</li><li>Contract</li><li>Freelance</li><li>Full-Time</li><li>Part-Time</li><li>Temporary</li></ul>
    <p class="copyright">© 2015 GREENLEAF JOBS. All Rights Reserved.</p>
  </footer>

</div>
</body>
</html>
```